Finiding oppertunites in Real Estate 6.15.20

size of ad 7” x 9.6”
1-I like the ad to stand out and attract people's attention.
2-you should be able to see the text of the ad clearly .. see the attachment anything in yellow is instructions.
3-the list of topics should not be the main part of the ad
4-if you decide you want a picture or vector of a person .. (you decide)
then it should be a white male about 25-30 years old wearing a solid white or blue shirt and not long hair.
5-leave 1 inch for footer
see attachment
Good luck

Target Market(s)

potential male students 25-35 years of age

Industry/Entity Type

Education

Requirements
Must have
• will stand out and people would want to see it.
should be able to read the words of ad
Nice to have
• how to make money in real estate on one line

```html
<!DOCTYPE html>
<html lang="en">
<head>
<meta charset="utf-8">
<title>Real Estate Career Course Flyer</title>
<link rel="stylesheet" href="https://fonts.googleapis.com/css2?family=Dosis:wght@200;300;700;800&family=Montserrat:wght@300&family=Cabin:wght@400;500&display=swap">
<style>
  :root {
    --yellow: #f3d416;
    --yellow-deep: #ecc90e;
    --teal: #234d5b;
    --white: #ffffff;
    --paper: #f4f4f2;
    --backdrop: #eeeeea;
  }
  * { margin: 0; padding: 0; box-sizing: border-box; }
  html, body { width: 1200px; height: 1200px; overflow: hidden; background: var(--backdrop); }
  .flyer {
    position: absolute; left: 162px; top: 0;
    width: 875px; height: 1200px;
    background: var(--yellow);
    overflow: hidden;
  }
  .title-band {
    position: absolute; left: 0; top: 0; width: 100%; height: 110px;
    display: flex; align-items: center; justify-content: center;
    font-family: "Dosis", sans-serif; font-weight: 800;
    font-size: 60px; letter-spacing: 0.5px; color: var(--teal);
    white-space: nowrap;
  }
  .main-panel {
    position: absolute; left: 15px; top: 110px; width: 845px; height: 930px;
    background: var(--teal);
  }
  .dash { display: block; width: 44px; height: 8px; background: var(--yellow); }
  .intro { position: absolute; left: 28px; top: 30px; width: 420px; }
  .intro .dash { margin-bottom: 18px; }
  .headline { font-family: "Dosis", sans-serif; line-height: 0.98; white-space: nowrap; }
  .headline .lead { display: block; font-family: "Montserrat", sans-serif; font-weight: 300; font-size: 44px; color: var(--white); margin-bottom: 6px; }
  .headline .accent { display: block; font-weight: 800; font-size: 88px; color: var(--yellow); letter-spacing: -1px; }
  .headline .strong { display: block; font-weight: 800; font-size: 66px; color: var(--white); }
  .intro .dash.second { margin: 22px 0 20px; }
  .pitch { font-family: "Cabin", sans-serif; font-size: 23px; line-height: 1.22; color: #e9eef0; text-align: justify; }
  .pitch + .pitch { margin-top: 10px; }
  .topics { position: absolute; left: 28px; top: 475px; width: 400px; }
  .topics .dash { margin-bottom: 16px; }
  .topics h2 { font-family: "Dosis", sans-serif; font-weight: 700; font-size: 27px; color: var(--white); margin-bottom: 8px; letter-spacing: 0.3px; white-space: nowrap; }
  .topics ul { list-style: none; font-family: "Cabin", sans-serif; font-size: 19px; line-height: 22px; color: #e4eaec; }
  .topics li { position: relative; padding-left: 20px; }
  .topics li::before { content: ""; position: absolute; left: 0; top: 8px; width: 8px; height: 8px; background: var(--yellow); }
  .photo {
    position: absolute; left: 470px; top: 130px; width: 370px; height: 555px;
    background: linear-gradient(160deg, #d9dcdd 0%, #b9bfc2 45%, #9fa6aa 100%);
  }
  .photo-stripe { position: absolute; right: 0; top: 40px; width: 70px; height: 515px; background: var(--yellow); opacity: 0.85; }
  .session-card {
    position: absolute; left: 455px; top: 700px; width: 405px; height: 410px;
    background: var(--paper); border-radius: 34px 0 0 0;
    display: flex; flex-direction: column; align-items: center;
    font-family: "Dosis", sans-serif; text-align: center; padding-top: 18px;
    white-space: nowrap;
  }
  .session-card .mode { font-weight: 200; font-size: 58px; color: var(--yellow-deep); line-height: 1; }
  .session-card .format { font-weight: 800; font-size: 72px; color: var(--yellow-deep); line-height: 1; margin-bottom: 12px; }
  .session-card .count {
    border-top: 2px solid var(--teal); border-bottom: 2px solid var(--teal);
    padding: 4px 12px; color: var(--teal); font-weight: 800; line-height: 1;
  }
  .session-card .count span { display: block; }
  .session-card .count .num { font-size: 40px; }
  .session-card .count .unit { font-size: 56px; }
  .session-card .start { font-family: "Montserrat", sans-serif; font-weight: 300; font-size: 30px; line-height: 1.2; color: var(--teal); margin-top: 14px; }
  .session-card .date { font-weight: 800; font-size: 70px; color: var(--yellow-deep); line-height: 1; }
</style>
</head>
<body>
  <article class="flyer">
    <header class="title-band">REAL ESTATE CAREER COURSE</header>
    <section class="main-panel">
      <div class="intro">
        <span class="dash"></span>
        <h1 class="headline">
          <span class="lead">HOW TO MAKE</span>
          <span class="accent">MONEY IN</span>
          <span class="strong">REAL ESTATE?</span>
        </h1>
        <span class="dash second"></span>
        <p class="pitch">For those who have started or would like to go into Real Estate.</p>
        <p class="pitch">An investment in knowledge opens up untold opportunities.</p>
      </div>
      <div class="topics">
        <span class="dash"></span>
        <h2>A PARTIAL LISTING OF TOPICS</h2>
        <ul>
          <li>Single-family</li>
          <li>Multifamily</li>
          <li>Management</li>
          <li>Real Estate Concepts</li>
          <li>Real Estate law</li>
          <li>Investment properties</li>
          <li>Foreclosures</li>
          <li>Rehab</li>
          <li>Foreclosures</li>
          <li>Short sales</li>
          <li>Development</li>
          <li>Finical modeling</li>
          <li>HUD properties</li>
          <li>Due Diligence</li>
        </ul>
      </div>
    </section>
    <div class="photo" role="img" aria-label="Photo of a young man in a white shirt holding a tablet, in a bright office">
      <span class="photo-stripe"></span>
    </div>
    <aside class="session-card">
      <span class="mode">REMOTE</span>
      <span class="format">SESSIONS</span>
      <div class="count">
        <span class="num">12 SESSION</span>
        <span class="unit">COURSE</span>
      </div>
      <span class="start">CLASSES STARTING</span>
      <span class="date">JUNE 16</span>
    </aside>
  </article>
</body>
</html>
```